Corporate Design für eine Hautarztpraxis gesucht
Die Zusammenarbeit mit TELUVI war geprägt von höchster Professionalität. Als erstes natürlich das Ergebnis, die Aussagekraft und die Anmutung des entworfenen Designs, da wurden die Anforderungen zu 100 % umgesetzt. Top-Kreativer mit Einfühlungsvermögen in den Kundenwunsch. Als zweites die Zusammenarbeit; verbindliche Kommunikation, die Designentwürfe wurden von TELUVI erklärt und er scheut nicht davor zurück, mitzuteilen wenn die Änderungswünsche vom Briefing und seiner Vorstellung der Umsetzung abweichen, prompte Reaktion auf Kommentare Als drittes die Zuverlässigkeit; alle Zusagen wurden eingehalten, auch das Feintuning nach Projektende war vorbildlich. Zusammenfassend: Top Designer, Vollprofi und 100% Zufriedenheit, danke und jederzeit gerne wieder!!! Working with TELUVI in the project was highly professional. First of all the result and the appearance of the logo and the printproducts; the job fullfillment has reached 100%. TELUVI is a top-creative with understanding and feeling for customer needs. Secondly working with him; the drafts were explained, communication to the point and fast responses to the remarks, and he was free in telling his opinion, if the remarks would lead in the wrong direction Third the reliability; everything was delivered, nothing missed, also the work and finetuning after the official end of the project was to our full satisfaction. Conclusion: Top designer, a real pro, 100 % satisfaction, thanks a lot and we would do it always again!!!
Zielgruppe
Neugründung einer Hautarztpraxis (Gemeinschaftspraxis) von drei Ärzten/Innen
Angeboten wird ein umfassendes medizinisches Spektrum für Kassen- und Privatpatienten sowie Dienstleistungen im Bereich Dermatologischer Kosmetik (Anti Aging, Lasertherapie, Botox, ...)
Die Zielgruppe besteht also zum einen Teil aus Patienten mit gesundheitlichen Problemen der Haut und Allergien sowie andererseits aus Kunden die kosmetische Dienstleistungen nachfragen.
Aufgabenstellung
In Bezug auf die Gestaltung sind wir sehr offen und haben noch keine konkrete Vorstellung, freuen uns aber über viele kreative Vorschläge, von denen wir uns den initialen Impuls für das Design des zukünftigen Logos erhoffen, welches dann im Projekt entwickelt werden soll.
Das Logo soll auf jeden Fall aus einer Wort- und Bildmarke bestehen (Prio 1), eventuell in ein Wappen/Emblem eingebunden sein (Prio 2).
Die Haut als menschliches Organ hat vielschichtige Funktionen, sie schützt den Organismus vor äußeren Umwelteinflüssen und repräsentiert den Menschen nach außen.
Die Haut steht auch für Sensibilität, Reinheit und Schönheit, diese Attribute könnten sich im Logo wiederfinden.
Das Logo soll Kompetenz, Seriosität, Eleganz und Sympathie ausstrahlen, dem Kunden Vertrauen vermitteln und im Verhältnis zur Wortmarke gleich stark sein, so dass z.B. bei der Visitenkarte und dem Briefpapier die Anordnung der Wort- zur Bildmarke unterschiedlich gestaltet werden kann.
Feedback können wir erst in den Abendstunden geben, da tagsüber gearbeitet werden muss und das aktuell noch in unterschiedlichen Arztpraxen.

```html
<!DOCTYPE html>
<html lang="de">
<head>
<meta charset="utf-8">
<title>Hautpraxis am See – Visitenkarte</title>
<link rel="stylesheet" href="https://fonts.googleapis.com/css2?family=Oswald:wght@400&family=Jost:ital,wght@1,400&display=swap">
<style>
  :root {
    --paper: #ffffff;
    --ink: #111111;
    --mark-grey: #444444;
    --frame-grey: #999999;
    --accent: #3bcfea;
  }
  * { margin: 0; padding: 0; box-sizing: border-box; }
  html, body { width: 1067px; height: 1200px; overflow: hidden; background: var(--paper); }
  .canvas { position: relative; width: 1067px; height: 1200px; background: var(--paper); }

  .card-front {
    position: absolute; left: 0; top: 250px; width: 1067px; height: 100px;
    display: flex; align-items: center; justify-content: center; gap: 18px;
  }
  .front-square {
    width: 44px; height: 44px; background: var(--accent); flex: none;
  }
  .front-name {
    font-family: "Oswald", sans-serif; font-weight: 400;
    font-size: 44px; line-height: 1; letter-spacing: 0.04em; color: var(--accent);
  }

  .card-back {
    position: absolute; left: 12px; top: 613px; width: 1042px; height: 571px;
    border: 4px solid var(--frame-grey);
  }
  .brand-name {
    position: absolute; left: 0; right: 0; top: 108px; text-align: center;
    font-family: "Oswald", sans-serif; font-weight: 400;
    font-size: 54px; line-height: 1.2; letter-spacing: 0.03em; color: var(--mark-grey);
  }
  .divider {
    position: absolute; left: 505px; top: 283px; width: 31px; height: 5px;
    background: var(--mark-grey);
  }
  .contact {
    position: absolute; left: 0; right: 0; top: 355px; text-align: center;
    font-family: "Jost", sans-serif; font-style: italic; font-weight: 400;
    font-size: 17px; letter-spacing: 0.5em; line-height: 30.5px; color: var(--ink);
  }
  .hours {
    position: absolute; left: 0; right: 0; top: 456px; text-align: center;
    font-family: "Jost", sans-serif; font-style: italic; font-weight: 400;
    font-size: 17px; letter-spacing: 0.5em; line-height: 29px; color: var(--accent);
    white-space: pre;
  }
</style>
</head>
<body>
<main class="canvas">
  <section class="card-front">
    <div class="front-square"></div>
    <div class="front-name">HAUTPRAXIS AM SEE</div>
  </section>

  <section class="card-back">
    <h1 class="brand-name">HAUTPRAXIS AM SEE</h1>
    <div class="divider"></div>
    <address class="contact">
      <div>SEEUFERWEG 14, 79102 FREIBURG</div>
      <div>TELEFON: 0761/5550127</div>
      <div>E-MAIL: INFO@HPSEE.DE</div>
    </address>
    <div class="hours"><div>MO   8-18 UHR</div><div>DI-FR   8-16 UHR</div></div>
  </section>
</main>
</body>
</html>
```